Business Card for Tutoring Company

We need a logo/symbol for an education company, along with an attractive business card. The logo should resemble both a pi symbol and the letter T.

Dear Designers,

I am narrowing down what I am looking for. 
I want the front of the card to be primarily white, with the company name "Maple Grove Learning" positioned towards the center.  The first letter, 'T' in 'Maple' will be modified so that it resembles a Pi symbol.
My personal information will be at the bottom.  If you think it fits, the website can be strewn across the top.

As for the back of the card, it will be primarily blue.  Toward the center will be the same T/pi shape engraved into a circular disk/button/emblem shape with some border.  It should be noted that I do like shiny blue, like the blue face of a Vantor.  Underneath the logo will be white text that reads, "Making Independent Learners and Thinkers."  At the very bottom of the card in smaller white font, the website "MapleGroveLearning.com" is written.

For more clarification, see my recent attachment.

Thank you.

Winston

Industry/Entity Type

Education

Logo styles of interest
Pictorial/Combination Logo
Requirements
Must have
• LOGO:
The logo is a solid blue circle with a symbol cutout from it. The cut out should closely resemble π and be the color white.

CARD:
The front has the logo in the top left corner, with "MAPLE GROVE LEARNING" written out beside it, spanning the width of the card. " At the bottom, personal information can be placed: Name, Title, Phone, Email.
The back has the the logo centered and enlarged. The website is printed "MapleGroveLearning.com
Nice to have
• LOGO:
It would be nice if the logo/pi symbol could be used as a letter T when spelling MGL or Maple Grove Learning.

CARD:
The enlarged logo on the back of the card can be enhanced (i.e. the blue is not solid blue but shiny, like the metallic blue face of a vantor) It would also be nice if the logo had a cool background (i.e. instead of the cutout of the pi-shape being white, it could be outerspace or something. Also, a motto "Growing Curious Minds and Bold Thinkers" printed under "MapleGroveLearning.com" would be nice, if it fits.

```html
<!DOCTYPE html>
<html lang="en">
<head>
<meta charset="utf-8">
<title>Maple Grove Learning – Business Card</title>
<link href="https://fonts.googleapis.com/css2?family=Figtree:wght@400&family=Pinyon+Script&display=swap" rel="stylesheet">
<style>
  :root {
    --page: #ffffff;
    --card-white: #ffffff;
    --brand-blue: #4150a0;
    --brand-blue-text: #3d4ba0;
    --ink: #151515;
    --tint-front: #dcdbef;
    --tint-back: #5a67b0;
    --web-text: #dfe2f3;
    --shadow: rgba(0, 0, 0, 0.28);
  }
  html, body {
    margin: 0;
    padding: 0;
    width: 1200px;
    height: 1000px;
    overflow: hidden;
    background: var(--page);
    font-family: "Figtree", "Helvetica Neue", Arial, sans-serif;
  }
  .stage {
    position: relative;
    width: 1200px;
    height: 1000px;
  }
  .card {
    position: absolute;
    left: 310px;
    width: 591px;
    height: 365px;
    overflow: hidden;
    box-shadow: 0 2px 8px var(--shadow);
  }
  .card--front { top: 91px; background: var(--card-white); }
  .card--back { top: 521px; background: var(--brand-blue); }

  .initial-mark {
    position: absolute;
    border-radius: 46% 54% 40% 60% / 30% 35% 65% 70%;
  }
  .card--front .initial-mark {
    left: 300px; top: 40px; width: 265px; height: 305px;
    background: linear-gradient(160deg, var(--tint-front), rgba(220, 219, 239, 0.5));
  }
  .card--back .initial-mark {
    left: 300px; top: 24px; width: 280px; height: 320px;
    background: linear-gradient(160deg, var(--tint-back), rgba(90, 103, 176, 0.45));
  }

  .brand {
    position: absolute;
    display: flex;
    align-items: center;
  }
  .brand__dot {
    border-radius: 50%;
    flex: none;
  }
  .card--front .brand { left: 150px; top: 44px; }
  .card--front .brand__dot {
    width: 38px; height: 38px;
    background: var(--brand-blue);
    margin-right: 12px;
  }
  .card--front .brand__name {
    font-size: 19px;
    letter-spacing: 0.3px;
    color: var(--brand-blue-text);
    white-space: nowrap;
  }

  .headline {
    position: absolute;
    left: 64px; top: 136px;
    margin: 0;
    font-weight: 400;
    font-size: 37px;
    color: var(--ink);
    white-space: nowrap;
  }
  .contact {
    position: absolute;
    left: 59px; top: 222px;
    color: var(--ink);
  }
  .contact__name { font-size: 22px; line-height: 28px; }
  .contact__title { font-size: 16px; line-height: 22px; margin-bottom: 20px; }
  .contact__line { font-size: 16.5px; line-height: 22px; }

  .card--back .brand { left: 50px; top: 146px; }
  .card--back .brand__dot {
    width: 70px; height: 70px;
    background: #ffffff;
    margin-right: 16px;
  }
  .card--back .brand__name {
    font-size: 22px;
    letter-spacing: 0.3px;
    color: #ffffff;
    white-space: nowrap;
  }
  .motto {
    position: absolute;
    left: 272px; top: 219px;
    font-family: "Pinyon Script", "Times New Roman", cursive;
    font-size: 18px;
    color: #ffffff;
    white-space: nowrap;
  }
  .website {
    position: absolute;
    right: 30px; top: 324px;
    font-size: 13px;
    color: var(--web-text);
  }
</style>
</head>
<body>
<main class="stage">
  <section class="card card--front" aria-label="Card front">
    <div class="initial-mark" role="img" aria-label="Large faint script initial"></div>
    <div class="brand">
      <span class="brand__dot"></span>
      <span class="brand__name">MAPLE GROVE LEARNING</span>
    </div>
    <h1 class="headline">Premier Education Services</h1>
    <div class="contact">
      <div class="contact__name">Winston Hartley</div>
      <div class="contact__title">Educational Consultant</div>
      <div class="contact__line">(555) 014 2387</div>
      <div class="contact__line">winston@MGLbest.com</div>
    </div>
  </section>

  <section class="card card--back" aria-label="Card back">
    <div class="initial-mark" role="img" aria-label="Large faint script initial"></div>
    <div class="brand">
      <span class="brand__dot"></span>
      <span class="brand__name">Maple Grove Learning</span>
    </div>
    <div class="motto">"Growing Curious Minds and Bold Thinkers"</div>
    <div class="website">MapleGroveLearning.com</div>
  </section>
</main>
</body>
</html>
```